KT Crewing business card

Require business card which includes:
Company name: KT CREWING PTY LTD
Email: Mick@ktcrewing.com.au
Phone: 0431 556 208
ACN: 517 238 649

slogan: Onsite Auto Electrician Labour hire

Details and logo on top side
Logo only on bottom side

colour codes : #F15A29 , #939598

Target Market(s)

Western Australia mining sector

Industry/Entity Type

Mining

Contact Information for Business Card

Require business card which includes: Company name: KT CREWING PTY LTD Email: Mick@ktcrewing.com.au Phone: 0431 556 208 ACN: 517 238 649 slogan: Onsite Auto Electrician Labour hire Details and logo on top side Logo only on bottom side colour codes : #F15A29 , #939598

Colors
EE7325
F08F49
F5BC92
FAE3D3
FDF4ED

Requirements
Must have
• double sided

```html
<!DOCTYPE html>
<html lang="en">
<head>
<meta charset="utf-8">
<title>KT Crewing business card</title>
<link href="https://fonts.googleapis.com/css2?family=Montserrat:wght@400;700;800&display=swap" rel="stylesheet">
<style>
  :root{
    --orange:#F15A29;
    --orange-deep:#E24E1F;
    --grey:#939598;
    --text-grey:#6d6e71;
    --card-white:#ffffff;
    --backdrop:#2a2b30;
  }
  *{margin:0;padding:0;box-sizing:border-box}
  html,body{width:1200px;height:817px;overflow:hidden}
  body{
    background:var(--backdrop);
    font-family:"Montserrat",sans-serif;
    display:flex;align-items:center;justify-content:center;gap:50px;
  }
  .card{
    width:540px;height:309px;border-radius:30px;position:relative;overflow:hidden;
  }
  .card--front{background:var(--card-white)}
  .card--back{background:var(--orange);display:flex;align-items:center;justify-content:center}

  .brand{
    position:absolute;top:42px;left:0;right:0;
    display:flex;align-items:center;justify-content:center;gap:12px;
  }
  .brand__square{width:22px;height:22px;background:var(--grey)}
  .brand__name{font-weight:800;font-size:42px;color:var(--orange);letter-spacing:-.5px;line-height:1}

  .company{
    position:absolute;top:124px;left:0;right:0;text-align:center;
    font-weight:800;font-size:22px;color:var(--orange);letter-spacing:.5px;
  }
  .contacts{
    position:absolute;top:166px;left:0;right:0;
    display:flex;justify-content:center;gap:22px;
    font-size:13px;color:var(--text-grey);
  }
  .contact{display:flex;align-items:center;gap:6px}
  .contact svg{width:16px;height:16px}
  .acn{
    position:absolute;top:196px;left:0;right:0;text-align:center;
    font-size:13px;color:var(--text-grey);
  }
  .acn__number{color:var(--orange)}
  .rule{position:absolute;top:247px;left:0;right:0;height:1px;background:var(--grey)}
  .slogan{
    position:absolute;top:235px;left:50%;transform:translateX(-50%);
    background:var(--card-white);border:1px solid var(--grey);
    padding:3px 10px;font-size:13.5px;color:var(--text-grey);white-space:nowrap;letter-spacing:.3px;
  }

  .back__name{font-weight:800;font-size:58px;color:var(--orange-deep);letter-spacing:-.5px}
</style>
</head>
<body>
  <section class="card card--front" aria-label="Card front">
    <div class="brand">
      <span class="brand__square"></span>
      <span class="brand__name">KT Crewing</span>
    </div>
    <h1 class="company">KT CREWING PTY LTD</h1>
    <div class="contacts">
      <span class="contact">
        <svg viewBox="0 0 16 16" aria-hidden="true"><circle cx="8" cy="8" r="8" fill="#F15A29"/><path d="M5.2 4.3l1.4 1.6-.7 1c.5 1 1.2 1.7 2.2 2.2l1-.7 1.6 1.4-.8 1.3c-2.8-.3-4.8-2.3-5.1-5.1z" fill="#fff"/></svg>
        0431 556 208
      </span>
      <span class="contact">
        <svg viewBox="0 0 16 16" aria-hidden="true"><circle cx="8" cy="8" r="8" fill="#F15A29"/><rect x="4" y="5.2" width="8" height="5.6" rx=".6" fill="#fff"/><path d="M4.3 5.6L8 8.4l3.7-2.8" stroke="#F15A29" stroke-width=".9" fill="none"/></svg>
        mick@ktcrewing.com.au
      </span>
    </div>
    <p class="acn">ACN: <span class="acn__number">517 238 649</span></p>
    <div class="rule"></div>
    <p class="slogan">Onsite Auto Electrician Labour Hire</p>
  </section>

  <section class="card card--back" aria-label="Card back">
    <span class="back__name">KT Crewing</span>
  </section>
</body>
</html>
```